New Corporate Brochure for Insurance and Employee Benefits company

Need a new brochure for an insurance/retirement planning company. We deal with upper management and business owners, as well as all of their employees and families. The brochure needs to be professional looking, but also some family friendly illustrations as well. Our corporate colors are dark forest green and metallic gold. Our website is www.tkhalvorsen-example.com

Target Market(s)

Company Executives and Business Owners

Industry/Entity Type

Business

Font styles to use
Serif

Requirements
Must have
• i want the brochure to be 11x17 folded to be 8.5 x 11 with four sides.

```html
<!DOCTYPE html>
<html lang="en">
<head>
<meta charset="utf-8">
<title>T.K. Halvorsen Associates Inc – Folder</title>
<link href="https://fonts.googleapis.com/css2?family=Cinzel:wght@400;600;700&display=swap" rel="stylesheet">
<style>
  :root {
    --forest: #2d3b1e;
    --forest-deep: #26331a;
    --gold: #b8965a;
    --gold-light: #ecd9a0;
    --gold-dark: #a8824a;
    --paper: #ffffff;
    --backdrop: #e6e6e6;
  }
  * { margin: 0; padding: 0; box-sizing: border-box; }
  html, body {
    width: 1200px; height: 1006px; overflow: hidden;
    background: var(--backdrop);
    font-family: "Cinzel", "Times New Roman", serif;
  }
  .folder {
    position: absolute; left: 44px; top: 143px;
    width: 1112px; height: 720px;
    background: var(--paper);
    box-shadow: 0 14px 30px rgba(0,0,0,0.18);
  }
  .folder-art { position: absolute; inset: 0; width: 1112px; height: 720px; }
  .panel { position: absolute; top: 0; width: 556px; height: 720px; }
  .panel-back { left: 0; }
  .panel-front { left: 556px; }

  .brand { text-align: center; color: var(--forest); }
  .brand-name { font-weight: 600; letter-spacing: 0.5px; line-height: 1; }
  .brand-assoc {
    display: flex; align-items: center; justify-content: center; gap: 8px;
    color: var(--gold); letter-spacing: 3px;
  }
  .brand-assoc::before, .brand-assoc::after {
    content: ""; height: 2px; background: var(--gold); flex: 1;
  }
  .brand-tagline { letter-spacing: 3.5px; font-weight: 600; }

  .panel-back .brand { position: absolute; left: 148px; top: 258px; width: 260px; }
  .panel-back .brand-name { font-size: 25px; }
  .panel-back .brand-assoc { font-size: 8px; margin-top: 3px; letter-spacing: 2px; }
  .panel-back .brand-tagline { font-size: 7px; margin-top: 3px; letter-spacing: 2.2px; }

  .contact {
    position: absolute; left: 0; top: 330px; width: 556px;
    text-align: center; font-size: 11px; line-height: 15px; color: #1d1d1d;
  }
  .social { display: flex; justify-content: center; gap: 8px; margin-top: 8px; }
  .social span { width: 17px; height: 17px; border-radius: 50%; background: var(--gold); }

  .panel-front .brand { position: absolute; left: 130px; top: 190px; width: 300px; }
  .panel-front .brand-name { font-size: 40px; }
  .panel-front .brand-assoc { font-size: 14px; margin-top: 4px; }
  .panel-front .brand-tagline { font-size: 11px; margin-top: 4px; }

  .web-address {
    position: absolute; bottom: 30px; left: 0; width: 556px;
    text-align: center; color: #ffffff; font-size: 13px; letter-spacing: 0.5px;
  }
</style>
</head>
<body>
  <div class="folder">
    <svg class="folder-art" viewBox="0 0 1112 720" xmlns="http://www.w3.org/2000/svg">
      <defs>
        <linearGradient id="goldSweep" x1="0" y1="0" x2="1" y2="0">
          <stop offset="0" stop-color="var(--gold-dark)"/>
          <stop offset="0.5" stop-color="#d2b57a"/>
          <stop offset="0.7" stop-color="var(--gold-light)"/>
          <stop offset="1" stop-color="var(--gold-dark)"/>
        </linearGradient>
        <linearGradient id="photoTone" x1="0" y1="0" x2="1" y2="0">
          <stop offset="0" stop-color="#e8c6a8"/>
          <stop offset="0.45" stop-color="#b9c6d6"/>
          <stop offset="1" stop-color="#a0705a"/>
        </linearGradient>
      </defs>
      <path d="M556,340 Q800,315 1112,322 L1112,520 L556,520 Z" fill="url(#photoTone)" role="img" aria-label="Photo: a smiling advisor reviewing documents with an older couple"/>
      <path d="M0,520 Q260,400 556,345 L556,720 L0,720 Z" fill="url(#goldSweep)"/>
      <path d="M0,565 Q300,450 556,432 C800,430 1000,470 1112,480 L1112,720 L0,720 Z" fill="var(--forest)"/>
      <path d="M0,590 Q280,510 556,500 Q850,500 1112,615 L1112,655 Q850,535 556,528 Q280,535 0,605 Z" fill="url(#goldSweep)"/>
    </svg>

    <section class="panel panel-back">
      <div class="brand">
        <div class="brand-name">T.K. Halvorsen</div>
        <div class="brand-assoc">Associates Inc</div>
        <div class="brand-tagline">Employee Benefit Advisors</div>
      </div>
      <div class="contact">
        <p>2218 Birchwood Lane, Maplefield, PA 16001</p>
        <p>Phone: (555) 014-2280 | Fax: (555) 014-2291</p>
        <div class="social"><span></span><span></span><span></span></div>
      </div>
      <p class="web-address">www.tkhalvorsen-example.com</p>
    </section>

    <section class="panel panel-front">
      <div class="brand">
        <div class="brand-name">T.K. Halvorsen</div>
        <div class="brand-assoc">Associates Inc</div>
        <div class="brand-tagline">Employee Benefit Advisors</div>
      </div>
      <p class="web-address">www.tkhalvorsen-example.com</p>
    </section>
  </div>
</body>
</html>
```